Expedition Cruise Sales Website for the Polar Regions (Antarctica & Arctic)

This will be a website for selling cruises.
This site should have a homepage, a ship page, destinations, and itineraries.
I have created a file specifying each page, and it is attached.
Pages:
1. Home
2. Cruise Lines
- 2.1 Ships
3. Destinations
- 3.1 Region - 3.2 Country - 3.3 City
4. Itineraries
- 4.1 Itinerary
5. Blog / Travel Tips 6. About Us
7. Contact
Please take a look on the attached pdf
Target Market(s)
Expedition Travelers
Coding
Coded - Design and coding required
Number of Pages Required
5+ page

```html
<!DOCTYPE html>
<html lang="en">
<head>
<meta charset="utf-8">
<title>Polarvia — Find your dream cruise</title>
<link href="https://fonts.googleapis.com/css2?family=Poppins:wght@400;500;600;700&family=Inter:wght@400;500;600&display=swap" rel="stylesheet">
<style>
:root{
  --blue:#3371bd;
  --blue-dark:#1f4f8f;
  --navy:#16243f;
  --ink:#1b1f2a;
  --muted:#8a93a3;
  --panel:#cfdcee;
  --band:#dce6f3;
  --line:#e4e9f1;
  --white:#ffffff;
  --star:#f0a020;
}
*{margin:0;padding:0;box-sizing:border-box}
html,body{width:1200px;height:4644px;overflow:hidden;background:var(--white)}
body{position:relative;font-family:"Inter",sans-serif;color:var(--ink)}
.abs{position:absolute}
.photo{position:absolute;overflow:hidden}
h1,h2,h3,.brand,.btn{font-family:"Poppins",sans-serif}
.accent{color:var(--blue)}

/* header */
.site-header{left:0;top:0;width:1200px;height:62px;background:var(--white)}
.brand{position:absolute;display:flex;align-items:center;gap:7px;font-weight:600;color:var(--blue)}
.brand-mark{width:16px;height:16px;background:var(--blue);border-radius:50%}
.nav{position:absolute;left:378px;top:24px;display:flex;gap:0;font-size:10px;font-weight:500}
.nav a{color:var(--ink);text-decoration:none;margin-right:48px}
.nav a.active{color:var(--blue)}
.header-phone{position:absolute;left:905px;top:23px;font-size:11px;font-weight:600;color:var(--blue)}
.btn{position:absolute;display:flex;align-items:center;justify-content:center;background:var(--blue);color:var(--white);font-size:10px;font-weight:500;border-radius:2px}

/* hero */
.hero{left:0;top:62px;width:1200px;height:406px;background:linear-gradient(180deg,#5d7594 0%,#8aa0bb 35%,#3f5878 62%,#1e3352 100%)}
.hero-title{left:0;width:1200px;top:195px;text-align:center;color:var(--white);font-size:38px;font-weight:600}
.hero-sub{left:0;width:1200px;top:250px;text-align:center;color:var(--white);font-size:13px}

.search{left:63px;top:405px;width:1074px;height:126px;background:var(--white);box-shadow:0 6px 20px rgba(20,40,80,.12)}
.search-title{position:absolute;left:0;width:100%;top:22px;text-align:center;font-size:11px;font-weight:600}
.field{position:absolute;top:58px;width:159px;height:35px;background:#d4e1f1;font-size:9px;padding:0 12px;display:flex;align-items:center;justify-content:space-between;color:var(--ink)}
.field span.ic{font-size:9px;color:#334}

/* section headings */
.sec-title{position:absolute;left:0;width:1200px;text-align:center;font-size:29px;font-weight:600;color:var(--ink)}
.sec-sub{position:absolute;left:0;width:1200px;text-align:center;font-size:11px;font-weight:500}

/* featured */
.feature-panel{left:263px;top:605px;width:674px;height:577px;background:var(--panel)}
.card{position:absolute;width:249px;background:var(--white);box-shadow:0 2px 10px rgba(20,40,80,.06)}
.card .photo{left:0;top:0;width:249px;height:155px}
.card-title{position:absolute;left:19px;font-size:11px;font-weight:600}
.card-text{position:absolute;left:19px;width:215px;font-size:8.5px;line-height:1.45;color:var(--muted)}
.price{position:absolute;left:19px;font-size:8.5px;color:var(--blue)}
.price b{font-weight:600}
.go{position:absolute;width:28px;height:28px;border-radius:50%;background:#dfe8f4;border:1px solid #c9d7ea;color:var(--blue);font-size:12px;display:flex;align-items:center;justify-content:center}
.dots{position:absolute;display:flex;gap:6px}
.dots i{width:8px;height:8px;border-radius:50%;background:#a9b3c2}
.dots i.on{background:var(--blue)}

/* destinations */
.dest{position:absolute;width:312px;height:219px}
.dest-label{position:absolute;left:0;top:163px;width:124px;height:28px;background:var(--white);font-family:"Poppins",sans-serif;font-weight:600;font-size:12px;letter-spacing:.5px;display:flex;align-items:center;padding-left:18px}

/* deals */
.deals-band{left:0;top:1987px;width:1200px;height:597px;background:linear-gradient(180deg,#d8e3f1 0%,#e8eef7 50%,#d3dfee 100%)}
.deal .line-name{position:absolute;left:19px;top:176px;font-family:"Poppins",sans-serif;font-size:17px;font-weight:600;color:var(--navy)}
.deal .price{font-size:11px}
.deal .price b{font-size:19px;font-weight:600}
.faded{opacity:.55}
.arrow-sm{position:absolute;width:22px;height:22px;border-radius:50%;background:var(--white);border:1px solid #c9d3e0;font-size:10px;display:flex;align-items:center;justify-content:center;color:#333}

/* reviews */
.review{position:absolute;width:249px;height:246px;background:var(--white);box-shadow:0 2px 14px rgba(20,40,80,.10);text-align:center}
.avatar{position:absolute;width:60px;height:60px;border-radius:50%;background:linear-gradient(160deg,#d8b89a,#8a6a55);border:3px solid var(--white)}
.stars{color:var(--star);font-size:13px;letter-spacing:2px}
.review .stars{position:absolute;left:0;width:100%;top:44px}
.review p{position:absolute;left:22px;width:205px;top:82px;font-size:8.5px;line-height:1.6}
.review .who{position:absolute;left:0;width:100%;top:172px;font-size:10px;font-weight:600}
.review .role{position:absolute;left:0;width:100%;top:190px;font-size:8px;color:var(--muted)}
.arrow-lg{position:absolute;width:26px;height:26px;border-radius:50%;border:1px solid #555;font-size:11px;display:flex;align-items:center;justify-content:center}

/* articles */
.article-title{position:absolute;left:19px;width:210px;font-size:11.5px;font-weight:600;line-height:1.3}

/* newsletter */
.news-band{left:0;top:3868px;width:1200px;height:423px;background:var(--blue)}
.news-title{left:106px;top:3945px;color:var(--white);font-family:"Poppins",sans-serif;font-size:28px;font-weight:400;line-height:1.2}
.news-sub{left:106px;top:4036px;width:390px;color:var(--white);font-size:10px;line-height:1.3}
.input{position:absolute;width:234px;height:31px;background:var(--white);font-size:8.5px;color:#333;display:flex;align-items:center;padding-left:13px}
.chat{left:1058px;top:4262px;width:112px;height:48px;background:var(--white);border-radius:4px;box-shadow:0 2px 8px rgba(0,0,0,.2);font-size:8px;padding:8px 0 0 8px;line-height:1.15}
.chat-dot{left:1122px;top:4250px;width:34px;height:34px;border-radius:50%;background:#2fb34a}

/* footer */
.footer{left:0;top:4291px;width:1200px;height:353px;background:linear-gradient(180deg,#22365a 0%,#1b2c4b 60%,#182741 100%);color:var(--white)}
.foot-text{left:106px;top:4425px;width:370px;font-size:9px;line-height:1.9;color:#dfe6f1}
.foot-h{font-family:"Poppins",sans-serif;font-size:12px;font-weight:500;color:var(--white)}
.foot-list{font-size:8.5px;line-height:19px;color:#dfe6f1;list-style:none}
.social{position:absolute;width:28px;height:28px;border-radius:50%;border:1px solid #cfd8e6}
.copy{left:106px;top:4603px;font-size:8.5px;color:#dfe6f1}
</style>
</head>
<body>

<header class="abs site-header">
  <div class="brand" style="left:62px;top:20px;font-size:15px"><span class="brand-mark"></span>Polarvia</div>
  <nav class="nav">
    <a class="active" href="#">Home</a><a href="#">Cruise lines</a><a href="#">Destinations</a><a href="#">Itineraries</a><a href="#">Blog</a><a href="#">About us</a><a href="#">Contact</a>
  </nav>
  <div class="header-phone">
    <svg width="10" height="10" viewBox="0 0 24 24" style="vertical-align:-1px"><path fill="#3371bd" d="M6.6 10.8a15 15 0 0 0 6.6 6.6l2.2-2.2c.3-.3.7-.4 1-.2 1.1.4 2.3.6 3.6.6.6 0 1 .4 1 1V20c0 .6-.4 1-1 1A17 17 0 0 1 3 4c0-.6.4-1 1-1h3.5c.6 0 1 .4 1 1 0 1.3.2 2.5.6 3.6.1.3 0 .7-.2 1z"/></svg>
    555.018.2040</div>
  <div class="btn" style="left:1025px;top:16px;width:100px;height:30px">Book Now!</div>
</header>

<section class="photo hero" role="img" aria-label="Expedition ship sailing past snowy polar mountains"></section>
<h1 class="abs hero-title">Find your dream cruise</h1>
<p class="abs hero-sub">From popular cruise lines to luxury voyages</p>

<form class="abs search">
  <div class="search-title">Explore 800+ Cruise Holidays</div>
  <div class="field" style="left:43px">Destination <span class="ic">⌾</span></div>
  <div class="field" style="left:209px">Port of Departure <span class="ic">⌄</span></div>
  <div class="field" style="left:374px">Dates <span class="ic">▦</span></div>
  <div class="field" style="left:540px">Duration <span class="ic">⌄</span></div>
  <div class="field" style="left:707px">Cruise Lines <span class="ic">⌄</span></div>
  <div class="btn" style="left:871px;top:58px;width:159px;height:35px">FIND A CRUISE</div>
</form>

<!-- Featured -->
<section class="abs feature-panel"></section>
<h2 class="sec-title" style="top:680px">Featured <span class="accent">cruise offers</span></h2>
<p class="sec-sub" style="top:729px">Choose the cruise that's perfect for you</p>

<article class="card" style="left:200px;top:773px;height:293px">
  <div class="photo" role="img" aria-label="Expedition ship in deep blue water" style="background:linear-gradient(180deg,#8fb4d6,#2d5d8c)"></div>
  <div class="card-title" style="top:175px">Best Antarctic Cruises</div>
  <div class="card-text" style="top:197px">Lorem ipsum is simply dummy text of the printing and typesetting industry.</div>
  <div class="price" style="top:252px">from <b>$1,139.00*</b></div>
  <div class="go" style="left:199px;top:243px">→</div>
</article>
<article class="card" style="left:475px;top:773px;height:293px">
  <div class="photo" role="img" aria-label="White cruise ship at sea under blue sky" style="background:linear-gradient(180deg,#a9c7e4,#3a6894)"></div>
  <div class="card-title" style="top:175px">Top Galápagos Cruises</div>
  <div class="card-text" style="top:197px">Lorem ipsum is simply dummy text of the printing and typesetting industry.</div>
  <div class="price" style="top:252px">from <b>$1200.00*</b></div>
  <div class="go" style="left:199px;top:243px">→</div>
</article>
<article class="card" style="left:750px;top:773px;height:293px">
  <div class="photo" role="img" aria-label="Cruise ship near a rocky coast" style="background:linear-gradient(180deg,#9cc0dc,#2e5677)"></div>
  <div class="card-title" style="top:175px">Last-Minute Deals</div>
  <div class="card-text" style="top:197px">Lorem ipsum is simply dummy text of the printing and typesetting industry.</div>
  <div class="price" style="top:252px">from <b>$980.00*</b></div>
  <div class="go" style="left:199px;top:243px">→</div>
</article>
<div class="dots" style="left:572px;top:1097px"><i></i><i class="on"></i><i></i><i></i></div>

<!-- Destinations -->
<h2 class="sec-title" style="top:1256px">Top cruise <span class="accent">destinations</span></h2>
<p class="sec-sub" style="top:1305px">Discover the breathtaking beauty of destinations with Aurora Line cruises.</p>

<div class="dest" style="left:106px;top:1369px"><div class="photo" role="img" aria-label="Bahamas resort towers above a tropical lagoon" style="inset:0;background:linear-gradient(180deg,#8fc0ea,#3f8a5c 60%,#2a6d8a)"></div><div class="dest-label">BAHAMAS</div></div>
<div class="dest" style="left:443px;top:1369px"><div class="photo" role="img" aria-label="Historic bridge over a river in Europe" style="inset:0;background:linear-gradient(180deg,#9cc6ea,#9e8a68 55%,#5a6a4a)"></div><div class="dest-label">EUROPE</div></div>
<div class="dest" style="left:780px;top:1369px"><div class="photo" role="img" aria-label="Caribbean beach with turquoise water" style="inset:0;background:linear-gradient(180deg,#4b8fd0,#3d8a55 45%,#7fd0d4 75%,#e6e0c8)"></div><div class="dest-label">CARIBBEAN</div></div>
<div class="dest" style="left:106px;top:1612px"><div class="photo" role="img" aria-label="Alaskan fjord between green mountains" style="inset:0;background:linear-gradient(180deg,#a8b8c6,#5e7a58 50%,#3b5a3e)"></div><div class="dest-label">ALASKA</div></div>
<div class="dest" style="left:443px;top:1612px"><div class="photo" role="img" aria-label="Ancient ruins on a Mexican cliff above the sea" style="inset:0;background:linear-gradient(135deg,#7fb0dc,#7a8a5a 45%,#45b0b8)"></div><div class="dest-label">MEXICO</div></div>
<div class="dest" style="left:780px;top:1612px"><div class="photo" role="img" aria-label="Waterfall mist in Canada" style="inset:0;background:linear-gradient(180deg,#5d6f80,#c9d4dc 50%,#3e5a6e)"></div><div class="dest-label">CANADA</div></div>

<div class="btn" style="left:531px;top:1881px;width:138px;height:30px">View All Destinations</div>

<!-- Cruise line deals -->
<section class="abs deals-band"></section>
<h2 class="sec-title" style="top:2060px">Cruise line <span class="accent">deals</span></h2>
<p class="sec-sub" style="top:2110px">Choose the cruise that's perfect for you — and get up to $1,000 to spend at sea</p>

<article class="card deal faded" style="left:-74px;top:2155px;height:305px">
  <div class="photo" role="img" aria-label="Guests dining on a ship deck" style="background:linear-gradient(180deg,#c9d4df,#8e9aa8)"></div>
  <div class="line-name" style="font-size:14px">Fjordway Cruise Line</div>
  <div class="card-text" style="top:218px">Lorem ipsum is simply dummy text of the printing and typesetting industry.</div>
  <div class="price" style="top:259px">from <b>$353</b></div>
  <div class="go" style="left:199px;top:256px">→</div>
</article>
<article class="card deal" style="left:200px;top:2155px;height:305px">
  <div class="photo" role="img" aria-label="Guests relaxing in a ship's pool" style="background:linear-gradient(180deg,#b8ccd9,#4f93b8)"></div>
  <div class="line-name">Harborline</div>
  <div class="card-text" style="top:218px">Lorem ipsum is simply dummy text of the printing and typesetting industry.</div>
  <div class="price" style="top:259px">from <b>$326</b></div>
  <div class="go" style="left:199px;top:256px">→</div>
</article>
<article class="card deal" style="left:475px;top:2155px;height:305px">
  <div class="photo" role="img" aria-label="Friends toasting on a sailing deck" style="background:linear-gradient(180deg,#c7d9e8,#8aa6be)"></div>
  <div class="line-name">Coral Crown</div>
  <div class="card-text" style="top:218px">Lorem ipsum is simply dummy text of the printing and typesetting industry.</div>
  <div class="price" style="top:259px">from <b>$271</b></div>
  <div class="go" style="left:199px;top:256px">→</div>
</article>
<article class="card deal" style="left:750px;top:2155px;height:305px">
  <div class="photo" role="img" aria-label="Guests dining outdoors on a cruise" style="background:linear-gradient(180deg,#c9d5df,#7e8e9c)"></div>
  <div class="line-name">Meridian</div>
  <div class="card-text" style="top:218px">Lorem ipsum is simply dummy text of the printing and typesetting industry.</div>
  <div class="price" style="top:259px">from <b>$279</b></div>
  <div class="go" style="left:199px;top:256px">→</div>
</article>
<article class="card deal faded" style="left:1025px;top:2155px;height:305px">
  <div class="photo" role="img" aria-label="Ship pool deck" style="background:linear-gradient(180deg,#b8ccd9,#4f93b8)"></div>
  <div class="line-name" style="font-size:14px">Starboard Cruises</div>
  <div class="card-text" style="top:218px">Lorem ipsum is simply dummy text of the printing and typesetting industry.</div>
  <div class="price" style="top:259px">from <b>$384</b></div>
</article>
<div class="arrow-sm" style="left:189px;top:2297px">‹</div>
<div class="arrow-sm" style="left:988px;top:2297px">›</div>
<div class="dots" style="left:572px;top:2492px"><i></i><i class="on"></i><i></i><i></i></div>

<!-- Reviews -->
<div class="abs" style="left:588px;top:2660px;width:24px;height:24px;border-radius:50%;background:var(--blue)"></div>
<h2 class="sec-title" style="top:2708px">Reviews from <span class="accent">happy passengers</span></h2>
<p class="sec-sub" style="top:2768px;font-size:9px">Excellent: <span class="stars" style="font-size:10px">★★★★★</span> 4.9 based on 600 reviews</p>

<div class="arrow-lg" style="left:143px;top:2955px">←</div>
<div class="arrow-lg" style="left:1030px;top:2955px">→</div>

<article class="review" style="left:200px;top:2862px">
  <div class="stars">★★★★★</div>
  <p>"It is a long established fact that a reader will be distracted by the readable content of a page when looking at its layout. the point of using lorem ipsum is that it has a more-or-less normal."</p>
  <div class="who">Standard Chunk</div><div class="role">Verified Customer</div>
</article>
<article class="review" style="left:475px;top:2862px">
  <div class="stars">★★★★★</div>
  <p>"It is a long established fact that a reader will be distracted by the readable content of a page when looking at its layout. the point of using lorem ipsum is that it has a more-or-less normal."</p>
  <div class="who">Finibus Bonorum</div><div class="role">Verified Customer</div>
</article>
<article class="review" style="left:750px;top:2862px">
  <div class="stars">★★★★★</div>
  <p>"It is a long established fact that a reader will be distracted by the readable content of a page when looking at its layout. the point of using lorem ipsum is that it has a more-or-less normal."</p>
  <div class="who">H. Rowan</div><div class="role">Verified Customer</div>
</article>
<div class="avatar" role="img" aria-label="Customer portrait" style="left:294px;top:2830px"></div>
<div class="avatar" role="img" aria-label="Customer portrait" style="left:569px;top:2830px;background:linear-gradient(160deg,#c9a88c,#4a4a4a)"></div>
<div class="avatar" role="img" aria-label="Customer portrait" style="left:844px;top:2830px;background:linear-gradient(160deg,#d4a88a,#6a3f30)"></div>

<div class="btn" style="left:549px;top:3142px;width:102px;height:30px">View All Review</div>

<!-- Articles -->
<h2 class="sec-title" style="top:3246px">Recent <span class="accent">articles</span></h2>
<p class="sec-sub" style="top:3292px;font-size:10px">Announcements &amp; press releases</p>

<article class="card" style="left:200px;top:3337px;height:336px">
  <div class="photo" role="img" aria-label="Expedition ship among icebergs" style="background:linear-gradient(180deg,#a9c4e0,#e4ecf3 55%,#3f6f9c)"></div>
  <div class="article-title" style="top:174px">Lorem ipsum is simply dummy text of the printing and typesetting</div>
  <div class="card-text" style="top:230px">It is a long established fact that a reader will be distracted by the readable content of a page when looking at its layout.</div>
  <div class="go" style="left:19px;top:285px">→</div>
</article>
<article class="card" style="left:475px;top:3337px;height:336px">
  <div class="photo" role="img" aria-label="White cruise ship under cloudy sky" style="background:linear-gradient(180deg,#7f9bb8,#d6dde4 60%,#4d6e8e)"></div>
  <div class="article-title" style="top:174px">Lorem ipsum is simply dummy text of the printing and typesetting</div>
  <div class="card-text" style="top:230px">It is a long established fact that a reader will be distracted by the readable content of a page when looking at its layout.</div>
  <div class="go" style="left:19px;top:285px">→</div>
</article>
<article class="card" style="left:750px;top:3337px;height:336px">
  <div class="photo" role="img" aria-label="Dark-hulled expedition ship at sea" style="background:linear-gradient(180deg,#8cb2d8,#2a4f7e 65%,#1b3558)"></div>
  <div class="article-title" style="top:174px">Lorem ipsum is simply dummy text of the printing and typesetting</div>
  <div class="card-text" style="top:230px">It is a long established fact that a reader will be distracted by the readable content of a page when looking at its layout.</div>
  <div class="go" style="left:19px;top:285px">→</div>
</article>

<div class="btn" style="left:549px;top:3706px;width:102px;height:30px">View All</div>

<!-- Newsletter -->
<section class="abs news-band"></section>
<div class="photo" role="img" aria-label="Expedition ship moored in a snowy polar bay" style="left:706px;top:3812px;width:387px;height:479px;background:linear-gradient(180deg,#dfe4ea 0%,#b8c3cf 40%,#5f7186 70%,#2f4058 100%)"></div>
<h2 class="abs news-title">Get cruise deals directly<br>in your inbox</h2>
<p class="abs news-sub">Subscribe now and set sail on a journey of endless adventure with our exclusive cruise newsletter</p>
<div class="input" style="left:106px;top:4092px">First Name</div>
<div class="input" style="left:353px;top:4092px">Last Name</div>
<div class="input" style="left:106px;top:4136px">Email Address...</div>
<div class="input" style="left:353px;top:4136px">Phone Number</div>
<div class="btn" style="left:106px;top:4209px;width:100px;height:29px;background:var(--navy)">Submit</div>

<div class="abs chat"><div style="font-size:7px">Available</div><div style="color:var(--blue);font-weight:600;font-size:12px">24/7 <span style="font-size:6px;color:#333;font-weight:400">to Assist with</span></div><div style="font-size:6px">Any Questions</div></div>
<div class="abs chat-dot"></div>

<!-- Footer -->
<footer class="abs footer"></footer>
<div class="brand" style="left:106px;top:4378px;font-size:24px;color:var(--white);gap:10px"><span class="brand-mark" style="width:30px;height:30px;background:var(--white)"></span>Polarvia</div>
<p class="abs foot-text">Lorem Ipsum is simply dummy text of the printing and typesetting industry. Lorem Ipsum has been the industry's standard dummy text ever since the 1500s, when an unknown printer took a galley of type and scrambled it to make a type specimen book.</p>

<div class="abs foot-h" style="left:587px;top:4364px">Contct Us</div>
<div class="abs" style="left:587px;top:4395px;font-size:10px;color:#dfe6f1">✆ &nbsp;555.018.2040</div>
<div class="abs" style="left:587px;top:4426px;font-size:9px;color:#dfe6f1">✉ &nbsp;support@polarviacruise.com</div>
<div class="abs foot-h" style="left:587px;top:4459px">Follow us</div>
<div class="social" style="left:589px;top:4497px"></div>
<div class="social" style="left:626px;top:4497px"></div>
<div class="social" style="left:663px;top:4497px"></div>
<div class="social" style="left:701px;top:4497px"></div>

<div class="abs foot-h" style="left:819px;top:4364px">Quick Links</div>
<ul class="abs foot-list" style="left:819px;top:4392px">
  <li>Home</li><li>Cruise Lines</li><li>Destinations</li><li>Itineraries</li><li>Blog</li><li>About Us</li><li>Contact</li>
</ul>
<ul class="abs foot-list" style="left:923px;top:4392px">
  <li>FAQ</li><li>Privacy Policy</li><li>Terms and Conditions</li><li>Booking Confirmation</li>
</ul>

<div class="abs copy">© 2025 <b>Polarvia</b> All Rights Reserved</div>
<svg class="abs" style="left:1128px;top:4560px" width="18" height="18" viewBox="0 0 20 20"><path d="M10 1 L18 19 L10 14 L2 19 Z" fill="#ffffff"/></svg>

</body>
</html>
```